Futuristic and Visually Appealing Photo Booth Rental Website

I need a Photo Booth rental website made for easy editing through Wordpress. Web design + Page Templates are needed for showcasing booths, packages, experiences, and add-ons. There's a space and futuristic theme to the company that I'd like to stick with. I'd like to integrate certain parts of the site with html code (iframe) but others with text, pictures, and video. I'd like the design as complete as possible while I help work on the content as much as I can. The priority should be making the site friendly enough to educate and convert sales/bookings. I have no problem working from a general photobooth website as a base.

Company: SnapTrek NX

Coding required. All source files needed to install as theme that can be edited by something like Elementor.

**Contact for current design done under maintenance mode**

Target Market(s)

All consumers (holiday parties, birthdays, weddings, etc...)
Corporate Clients (conventions, virtual expos, holiday parties, company events)

Industry/Entity Type

Events

Coding

Coded - Design and coding required

Font styles to use
Sans Serif

Requirements
Must have
• ===Menu/Submenu===
Our Booths: DSLR Open Air Photo Booth, Selfie Station, Drifta, Pendulum Skiv, LumaVex
Consumers: Rental Packages, Addons
Corporate: Experiences, Addons, Build-to-Suit, Get a Quote (iframe)
About: About Us, Non-Profits, Employment
Customizations: Printout Templates (iframe), Start Screens (iframe), Backdrops
Contact Us: Inquiry, Custom Quote

===Buttons/Call to Action===
Book Online
Find My Photos
Client Portal

Social Media Icons and Footer section for vendor buttons (vowlinker, quib, the plume, etc...)

Responsive design
Nice to have
• Video Slides on Frontpage
Should not have
• OnePage Design

```html
<!DOCTYPE html>
<html lang="en">
<head>
<meta charset="utf-8">
<title>SnapTrek NX – Professional Photo Booth</title>
<link href="https://fonts.googleapis.com/css2?family=Lato:wght@300;400;700;900&display=swap" rel="stylesheet">
<style>
:root{
  --space-dark:#05080f;
  --space-mid:#101a2c;
  --accent:#2a8ff0;
  --accent-cyan:#27b6f2;
  --ink:#222831;
  --muted:#6b7078;
  --line:#e3e5e8;
  --white:#ffffff;
  --navy:#0c1235;
  --form-dark:#1a1416;
}
*{box-sizing:border-box;margin:0;padding:0}
html,body{width:1200px;height:4164px;overflow:hidden}
body{font-family:'Lato',sans-serif;color:var(--ink);background:var(--white);position:relative}
.btn{display:inline-block;background:var(--accent);color:var(--white);font-size:11px;font-weight:700;letter-spacing:.6px;text-transform:uppercase;border-radius:18px;padding:11px 30px;text-decoration:none}

/* Hero */
.hero{position:absolute;left:0;top:0;width:1200px;height:800px;z-index:1;background:radial-gradient(ellipse at 60% 85%,#2a3a55 0%,var(--space-mid) 35%,var(--space-dark) 75%);overflow:hidden}
.site-nav{position:absolute;left:0;top:0;width:1200px;height:80px}
.brand{position:absolute;left:112px;top:6px;display:flex;align-items:center;gap:10px}
.brand-mark{width:66px;height:66px;border-radius:50%;background:#163244}
.brand-name{color:var(--white);font-size:15px;font-weight:700}
.menu{position:absolute;left:345px;top:58px;display:flex;gap:34px;list-style:none}
.menu li{color:var(--white);font-size:15px}
.menu li.caret::after{content:"";display:inline-block;margin-left:6px;border:4px solid transparent;border-top-color:var(--white);vertical-align:-2px}
.hero-copy{position:absolute;left:110px;top:425px;color:var(--white)}
.hero-copy .pre{font-size:24px;font-weight:400}
.hero-copy h1{font-size:46px;font-weight:400;color:var(--accent-cyan);letter-spacing:1px;line-height:1.1}
.hero-copy .post{font-size:24px}
.hero-copy p{font-size:11px;margin:18px 0 24px}
.collage div{position:absolute;border:3px solid #f2f2f2}
.hero-wave{position:absolute;left:0;bottom:0}

/* Services */
.services{position:absolute;left:0;top:810px;width:1200px;height:1080px;z-index:2}
.section-title{position:relative;z-index:3;text-align:center;font-size:26px;font-weight:400;color:var(--ink)}
.services-box{position:absolute;left:112px;top:55px;width:993px;height:1015px;border:1px solid var(--line)}
.service{position:absolute;width:290px;text-align:center}
.service .photo{width:290px;height:288px}
.service .btn{margin-top:38px;padding:9px 36px;font-size:10px}

/* Contact band */
.pay-band{position:absolute;left:0;top:1955px;width:1200px;height:580px;background:linear-gradient(110deg,#7c2a2d 0%,#b4494e 35%,#6c2b31 65%,#a23d44 100%);overflow:hidden}
.pay-band .shade{position:absolute;inset:0;background:rgba(20,10,12,.35)}
.pay-copy{position:absolute;left:0;top:210px;width:1200px;text-align:center;color:var(--white)}
.pay-copy h2{font-size:26px;font-weight:400}
.pay-copy p{font-size:11px;line-height:1.6;margin:12px 0 22px}
.btn-ghost{display:inline-block;border:1px solid var(--white);color:var(--white);font-size:10px;letter-spacing:.6px;text-transform:uppercase;border-radius:16px;padding:9px 22px}
.wave{position:absolute;left:0}

/* Events */
.events{position:absolute;left:0;top:2600px;width:1200px}
.event{position:absolute;top:110px;width:215px}
.event .photo{width:215px;height:145px}
.event h3{font-size:22px;font-weight:400;line-height:1.15;margin:18px 0 14px}
.event p{font-size:11px;line-height:1.6;color:var(--muted)}
.events .more{position:absolute;left:0;top:525px;width:1200px;text-align:center}

/* Contact form */
.get-in-touch{position:absolute;left:0;top:3225px;width:1200px;height:565px;background:radial-gradient(ellipse at 50% 60%,#4a2a30 0%,var(--form-dark) 70%);color:var(--white)}
.get-in-touch h2{text-align:center;font-size:26px;font-weight:400;padding-top:80px}
.get-in-touch .sub{text-align:center;font-size:12px;margin-top:8px}
.inquiry{position:absolute;left:100px;top:205px;width:990px}
.inquiry label{display:block;font-size:12px;margin-bottom:8px}
.field{background:var(--white);border-radius:6px;height:38px;margin-bottom:18px}
.field.tall{height:80px}
.inquiry .btn{padding:10px 30px;margin-top:-6px}

/* Footer */
.site-footer{position:absolute;left:0;top:3790px;width:1200px;height:374px;background:var(--navy);color:var(--white)}
.foot-col{position:absolute;top:85px}
.foot-col h4{font-size:14px;font-weight:700;letter-spacing:.8px;text-transform:uppercase;margin-bottom:22px}
.foot-col p{font-size:12px;line-height:1.6;width:230px}
.foot-col ul{list-style:none;font-size:13px;line-height:1.55}
.socials{display:flex;gap:8px}
.socials span{width:22px;height:22px;border-radius:3px}
</style>
</head>
<body>

<header class="hero">
  <nav class="site-nav">
    <div class="brand"><span class="brand-mark"></span><span class="brand-name">SnapTrek NX</span></div>
    <ul class="menu">
      <li class="caret">Our Booths</li>
      <li class="caret">Consumers</li>
      <li class="caret">Corporate</li>
      <li class="caret">About</li>
      <li class="caret">Customizations</li>
      <li class="caret">Contact Us</li>
    </ul>
  </nav>

  <div class="collage">
    <div role="img" aria-label="Guests posing in a photo booth strip" style="left:668px;top:170px;width:222px;height:128px;background:linear-gradient(135deg,#c8484f,#e8b7a8)"></div>
    <div role="img" aria-label="Friends posing in front of a red backdrop" style="left:922px;top:270px;width:142px;height:100px;background:linear-gradient(135deg,#b0313b,#e27c7c)"></div>
    <div role="img" aria-label="Photo booth kiosk at an event" style="left:665px;top:330px;width:108px;height:196px;background:linear-gradient(180deg,#4a4f5c,#a9a6a0)"></div>
    <div role="img" aria-label="Group of guests holding props" style="left:775px;top:420px;width:228px;height:112px;background:linear-gradient(135deg,#d9c7b8,#8c6e64)"></div>
    <div role="img" aria-label="Booth printouts and guests at a party" style="left:675px;top:540px;width:325px;height:170px;background:linear-gradient(135deg,#3b4150,#b08f86)"></div>
  </div>

  <div class="hero-copy">
    <div class="pre">Professional</div>
    <h1>PHOTO BOOTH</h1>
    <div class="post">for all Occasions</div>
    <p>We create fun and lasting memories to keep your guests buzzing for ages.</p>
    <a class="btn">Book Now</a>
  </div>

  <svg class="hero-wave" width="1200" height="80" viewBox="0 0 1200 80" aria-hidden="true">
    <path d="M0 15 C300 90 600 90 820 45 C1000 8 1120 8 1200 25 L1200 80 L0 80 Z" fill="#ffffff"/>
  </svg>
</header>

<section class="services">
  <h2 class="section-title">Our Services</h2>
  <div class="services-box"></div>
  <div class="service" style="left:128px;top:128px"><div class="photo" role="img" aria-label="Wedding couple at a photo booth" style="background:linear-gradient(160deg,#3a2e2a,#c9b7a4)"></div><a class="btn">Weddings</a></div>
  <div class="service" style="left:464px;top:128px"><div class="photo" role="img" aria-label="Graduates in caps and gowns" style="background:linear-gradient(160deg,#6b7060,#2b2a2e)"></div><a class="btn">Graduations</a></div>
  <div class="service" style="left:797px;top:128px"><div class="photo" role="img" aria-label="Friends at a festival booth" style="background:linear-gradient(160deg,#1e2a44,#b99c6a)"></div><a class="btn">Festivals</a></div>
  <div class="service" style="left:128px;top:560px"><div class="photo" role="img" aria-label="Birthday guests with props" style="background:linear-gradient(160deg,#b23a45,#e6c2b4)"></div><a class="btn">Birthdays</a></div>
  <div class="service" style="left:464px;top:560px"><div class="photo" role="img" aria-label="Fashion show guest on a printout template" style="background:linear-gradient(160deg,#e68aa0,#f5d6dc)"></div><a class="btn">Fashion Shows</a></div>
  <div class="service" style="left:797px;top:560px"><div class="photo" role="img" aria-label="Colleagues at a corporate event" style="background:linear-gradient(160deg,#d9d4cf,#3a3434)"></div><a class="btn">Corporate</a></div>
</section>

<section class="pay-band" role="img" aria-label="Guests wearing heart glasses in front of a red backdrop">
  <div class="shade"></div>
  <svg class="wave" style="top:0" width="1200" height="70" viewBox="0 0 1200 70" aria-hidden="true">
    <path d="M0 0 L1200 0 L1200 20 C900 70 650 60 420 30 C250 10 100 25 0 50 Z" fill="#ffffff"/>
  </svg>
  <div class="pay-copy">
    <h2>Contact us for payment arrangements.</h2>
    <p>A photo booth should be something you remember on your special day. Let us help you.<br>Bring the photo booth to your event and party.</p>
    <span class="btn-ghost">Get a Quote Now</span>
  </div>
  <svg class="wave" style="bottom:0" width="1200" height="80" viewBox="0 0 1200 80" aria-hidden="true">
    <path d="M0 50 C250 10 500 20 750 55 C950 80 1100 60 1200 30 L1200 80 L0 80 Z" fill="#ffffff"/>
  </svg>
</section>

<section class="events">
  <h2 class="section-title">Recent Events</h2>
  <article class="event" style="left:120px"><div class="photo" role="img" aria-label="Valentine's event printout" style="background:linear-gradient(135deg,#a8222c,#d45a5f)"></div><h3>Star Wings Valentine's Craft Night</h3><p>Lorem ipsum dolor sit amet, consectetur adipiscing elit. Ut elit tellus, luctus nec ullamcorper mattis, pulvinar dapibus leo.</p></article>
  <article class="event" style="left:370px"><div class="photo" role="img" aria-label="Expo booth printout" style="background:linear-gradient(135deg,#e8788c,#f7cfd6)"></div><h3>QuinceFiesta Expo 2020 - Las Vegas!</h3><p>Lorem ipsum dolor sit amet, consectetur adipiscing elit. Ut elit tellus, luctus nec ullamcorper mattis, pulvinar dapibus leo.</p></article>
  <article class="event" style="left:620px"><div class="photo" role="img" aria-label="Valentine's event printout" style="background:linear-gradient(135deg,#a8222c,#d45a5f)"></div><h3>Star Wings Valentine's Craft Night</h3><p>Lorem ipsum dolor sit amet, consectetur adipiscing elit. Ut elit tellus, luctus nec ullamcorper mattis, pulvinar dapibus leo.</p></article>
  <article class="event" style="left:870px"><div class="photo" role="img" aria-label="Expo booth printout" style="background:linear-gradient(135deg,#e8788c,#f7cfd6)"></div><h3>QuinceFiesta Expo 2020 - Las Vegas!</h3><p>Lorem ipsum dolor sit amet, consectetur adipiscing elit. Ut elit tellus, luctus nec ullamcorper mattis, pulvinar dapibus leo.</p></article>
  <div class="more"><a class="btn">View Gallery</a></div>
</section>

<section class="get-in-touch" role="img" aria-label="Party guests celebrating behind the contact form">
  <h2>Get in Touch</h2>
  <div class="sub">Booking a Booth or Getting More Info? Send Us a Message</div>
  <form class="inquiry">
    <label>Name</label><div class="field"></div>
    <label>Email</label><div class="field"></div>
    <label>Message</label><div class="field tall"></div>
    <a class="btn">Send</a>
  </form>
</section>

<footer class="site-footer">
  <div class="foot-col" style="left:110px">
    <h4>About Us</h4>
    <p>Lorem ipsum dolor sit amet, consectetur adipiscing elit, sed do eiusmod tempor incidi. Lorem ipsum dolor sit amet, consectetur adip.</p>
  </div>
  <div class="foot-col" style="left:440px">
    <h4>Menu</h4>
    <ul><li>Our Booths</li><li>Consumers</li><li>Corporate</li><li>About</li><li>Customizations</li><li>Contact Us</li></ul>
  </div>
  <div class="foot-col" style="left:775px">
    <h4>Social</h4>
    <div class="socials">
      <span aria-label="Social link" style="background:#555a63"></span>
      <span aria-label="Social link" style="background:#3b5fb0"></span>
      <span aria-label="Social link" style="background:#2ea3ea"></span>
      <span aria-label="Social link" style="background:#2a78c2"></span>
      <span aria-label="Social link" style="background:#e0457f"></span>
    </div>
  </div>
</footer>

</body>
</html>
```